Dunmore Plumbing LLC business card

Would like a modern looking business card with my new logo

Contact Information for Business Card

Calvin Dunmore 2418 Elm Hollow Rd Southbury, CT 06999, Dunmoreplumbingllc@exampletrade.com, 203-555-0174

```html
<!DOCTYPE html>
<html lang="en">
<head>
<meta charset="utf-8">
<title>Dunmore Plumbing LLC — Business Card</title>
<link rel="stylesheet" href="https://fonts.googleapis.com/css2?family=Roboto:wght@400;700;900&display=swap">
<style>
  :root {
    --page-bg: #2c2c2d;
    --card-top: #2b2c2e;
    --card-bottom: #1d1e20;
    --text-light: #e6e7e8;
    --text-soft: #d2d4d6;
    --logo-grey: #7d7f82;
    --accent-blue: #0a93cc;
    --strip-grey: #8a8b8d;
  }
  * { box-sizing: border-box; margin: 0; padding: 0; }
  html, body {
    width: 1200px; height: 1138px; overflow: hidden;
    background: var(--page-bg);
    font-family: "Roboto", Arial, sans-serif;
  }
  .card {
    position: absolute;
    width: 620px; height: 375px;
    border-radius: 14px;
    overflow: hidden;
    background: linear-gradient(160deg, var(--card-top), var(--card-bottom));
    box-shadow: 0 6px 14px rgba(0,0,0,.45);
  }
  .card--front { left: 272px; top: 184px; }
  .card--back  { left: 274px; top: 606px; }

  .wordmark {
    position: absolute;
    font-weight: 900;
    text-transform: uppercase;
    white-space: nowrap;
    letter-spacing: 1px;
  }
  .card--front .wordmark {
    left: 0; right: 0; top: 152px;
    text-align: center;
    font-size: 37px;
    color: var(--logo-grey);
  }
  .card--back .wordmark {
    left: 30px; top: 74px;
    font-size: 34px;
    color: var(--text-light);
  }

  .front-tagline {
    position: absolute; left: 0; right: 0; top: 326px;
    display: flex; justify-content: center; align-items: center; gap: 24px;
    font-size: 17px; color: var(--text-soft);
  }
  .front-tagline .rule {
    width: 70px; height: 2px; background: var(--accent-blue);
  }

  .contact-name {
    position: absolute; left: 30px; top: 202px;
    font-size: 26px; font-weight: 900; color: var(--accent-blue);
    text-transform: uppercase; letter-spacing: .5px;
  }
  .contact-title {
    position: absolute; left: 30px; top: 243px;
    font-size: 17px; color: var(--text-light);
  }
  .contact-address {
    position: absolute; left: 30px; top: 288px;
    font-size: 17px; line-height: 24px; color: var(--text-light);
  }
  .contact-lines {
    position: absolute; left: 292px; right: 14px; top: 262px;
    list-style: none; font-size: 15px; line-height: 24px; color: var(--text-light);
    white-space: nowrap;
  }
  .contact-lines li { display: flex; align-items: center; gap: 10px; }
  .contact-lines svg { width: 16px; height: 14px; fill: var(--accent-blue); flex: none; }

  .bottom-strip {
    position: absolute; left: 0; bottom: 0;
    width: 300px; height: 14px; background: var(--strip-grey);
  }
  .bottom-band {
    position: absolute; left: 266px; bottom: 0;
    width: 354px; height: 45px;
    background: var(--accent-blue);
    clip-path: polygon(20px 0, 100% 0, 100% 100%, 0 100%);
    display: flex; align-items: center; padding-left: 56px;
    font-size: 18px; font-weight: 700; color: var(--text-light);
  }
</style>
</head>
<body>
  <section class="card card--front" aria-label="Card front">
    <div class="wordmark">Dunmore Plumbing LLC</div>
    <div class="front-tagline">
      <span class="rule"></span>
      <span>Dunmore Plumbing LLC</span>
      <span class="rule"></span>
    </div>
  </section>

  <section class="card card--back" aria-label="Card back">
    <div class="wordmark">Dunmore Plumbing LLC</div>

    <h1 class="contact-name">Calvin Dunmore</h1>
    <p class="contact-title">Managing Director</p>
    <p class="contact-address">2418 Elm Hollow Rd<br>Southbury, CT 06999</p>

    <ul class="contact-lines">
      <li>
        <svg viewBox="0 0 16 14" aria-hidden="true"><path d="M1 4c0-2 3-3 7-3s7 1 7 3v1.5h-3.5V4H4.5v1.5H1z M4 6h8l2 7H2z"/></svg>
        <span>203-555-0174</span>
      </li>
      <li>
        <svg viewBox="0 0 16 14" aria-hidden="true"><path d="M1 2h14v10H1z M2 3l6 5 6-5" fill="none" stroke="#0a93cc" stroke-width="1.6"/></svg>
        <span>Dunmoreplumbingllc@exampletrade.com</span>
      </li>
    </ul>

    <div class="bottom-strip"></div>
    <div class="bottom-band">Dunmore Plumbing LLC</div>
  </section>
</body>
</html>
```